Ferncrest Dental, LLC business card project

Business card to be designed with current logo.
Dental office- please keep design of card that looks clean and professional.
Please include the following info:
Ferncrest Dental, LLC
Dr. Lorna Pettigrew
2871 Marlowe Street
Bethlehem, PA 18093
610-555-0193
ferncrestdental.office@examplemail.test
Hello everyone-
Reason: Just got back from overseas- will look at all designs and provide feedback. Thank you!
Reason: Polling my friends for the final selection-
thank you to all those that participated- so many talented designers!

```html
<!DOCTYPE html>
<html lang="en">
<head>
<meta charset="utf-8">
<title>Ferncrest Dental, LLC – Business Cards</title>
<link rel="stylesheet" href="https://fonts.googleapis.com/css2?family=Ubuntu:wght@300;500&family=Open+Sans:wght@400&display=swap">
<style>
  :root {
    --backdrop: #e6e7e5;
    --card: #ffffff;
    --green-dark: #5e9a3c;
    --green-mid: #7fb21f;
    --green-light: #9cc20a;
    --brand: #6aa92c;
    --name: #5f9c32;
    --ink: #333333;
    --mail-light: #8cc11a;
  }
  * { box-sizing: border-box; margin: 0; padding: 0; }
  html, body { width: 1200px; height: 900px; overflow: hidden; }
  body { background: var(--backdrop); position: relative; font-family: "Open Sans", sans-serif; }

  .card { position: absolute; background: var(--card); overflow: hidden; }

  .brand {
    display: flex; align-items: center; gap: 10px;
    font-family: "Ubuntu", sans-serif; font-weight: 300;
    color: var(--brand); white-space: nowrap; letter-spacing: -0.5px;
  }
  .brand__dot { width: 14px; height: 14px; border-radius: 50%; background: var(--brand); flex: none; }

  .band { position: absolute; left: 0; width: 100%; }
  .band--top { background: linear-gradient(90deg, var(--green-light), var(--green-mid)); }
  .band--bottom { background: linear-gradient(90deg, var(--green-dark), var(--green-mid)); }
  .band--top.band--rev { background: linear-gradient(90deg, var(--green-dark), var(--green-light)); }
  .band--bottom.band--rev { background: linear-gradient(90deg, var(--green-dark), var(--green-light)); }
  .strip { position: absolute; left: 0; width: 100%; display: flex; align-items: center; justify-content: center; }

  .contact { position: absolute; color: var(--ink); font-size: 12.5px; line-height: 17px; }
  .contact__name { font-family: "Ubuntu", sans-serif; font-weight: 500; color: var(--name); font-size: 14px; margin-bottom: 22px; }
  .contact__address { margin-bottom: 16px; }
  .contact__phone { margin-bottom: 10px; }
  .mail__user { color: var(--name); }
  .mail__domain { color: var(--mail-light); }

  /* vertical card */
  .card--vertical { left: 241px; top: 50px; width: 263px; height: 450px; }
  .card--vertical .brand { position: absolute; top: 58px; left: 0; width: 100%; justify-content: center; font-size: 24px; gap: 7px; }
  .card--vertical .brand__dot { width: 11px; height: 11px; }
  .card--vertical .contact { left: 20px; top: 173px; }
  .card--vertical .wave { position: absolute; left: 0; bottom: 0; width: 263px; height: 155px; }
  .card--vertical .wave-mail {
    position: absolute; left: 18px; right: 18px; bottom: 44px;
    color: #fff; font-size: 10px; text-align: center; white-space: nowrap;
  }

  /* horizontal banded card */
  .card--banded { left: 555px; top: 155px; width: 450px; height: 263px; }
  .card--banded .band--top { top: 0; height: 72px; }
  .card--banded .strip { top: 72px; height: 111px; }
  .card--banded .band--bottom { top: 183px; height: 80px; }
  .card--banded .brand { font-size: 32px; }

  /* rounded banded card */
  .card--rounded-band { left: 118px; top: 548px; width: 486px; height: 285px; border-radius: 95px 0 95px 0; }
  .card--rounded-band .band--top { top: 0; height: 93px; }
  .card--rounded-band .strip { top: 93px; height: 86px; }
  .card--rounded-band .band--bottom { top: 179px; height: 106px; }
  .card--rounded-band .brand { font-size: 34px; }

  /* rounded contact card */
  .card--rounded-contact { left: 618px; top: 458px; width: 486px; height: 286px; border-radius: 95px 0 95px 0; }
  .card--rounded-contact .brand { position: absolute; right: 36px; top: 36px; font-size: 32px; }
  .card--rounded-contact .contact { left: 54px; top: 100px; font-size: 13.5px; line-height: 18px; }
  .card--rounded-contact .contact__name { font-size: 14.5px; margin-bottom: 24px; }
</style>
</head>
<body>

  <section class="card card--vertical">
    <div class="brand"><span class="brand__dot"></span>Ferncrest Dental</div>
    <div class="contact">
      <p class="contact__name">Dr. Lorna Pettigrew</p>
      <p class="contact__address">2871 Marlowe Street<br>Bethlehem, PA 18093</p>
      <p class="contact__phone">610-555-0193</p>
    </div>
    <svg class="wave" viewBox="0 0 263 155" role="img" aria-label="Green wave panel with diamond pattern">
      <defs>
        <linearGradient id="waveFill" x1="0" x2="1" y1="0" y2="0">
          <stop offset="0" stop-color="#9cc20a"/>
          <stop offset="1" stop-color="#7fb21f"/>
        </linearGradient>
      </defs>
      <path d="M0 105 C30 40 90 25 150 38 C200 50 240 40 263 0 L263 155 L0 155 Z" fill="url(#waveFill)"/>
    </svg>
    <p class="wave-mail">ferncrestdental.office@examplemail.test</p>
  </section>

  <section class="card card--banded">
    <div class="band band--top" role="img" aria-label="Green band with diamond pattern"></div>
    <div class="strip"><div class="brand"><span class="brand__dot"></span>Ferncrest Dental</div></div>
    <div class="band band--bottom" role="img" aria-label="Green band with diamond pattern"></div>
  </section>

  <section class="card card--rounded-band">
    <div class="band band--top band--rev" role="img" aria-label="Green band with diamond pattern"></div>
    <div class="strip"><div class="brand"><span class="brand__dot"></span>Ferncrest Dental</div></div>
    <div class="band band--bottom band--rev" role="img" aria-label="Green band with diamond pattern"></div>
  </section>

  <section class="card card--rounded-contact">
    <div class="brand"><span class="brand__dot"></span>Ferncrest Dental</div>
    <div class="contact">
      <p class="contact__name">Dr. Lorna Pettigrew</p>
      <p class="contact__address">2871 Marlowe Street<br>Bethlehem, PA 18093</p>
      <p class="contact__phone">610-555-0193</p>
      <p class="contact__mail"><span class="mail__user">ferncrestdental.office</span><span class="mail__domain">@examplemail.test</span></p>
    </div>
  </section>

</body>
</html>
```